Brightpath Learning Data Dashboard

Brightpath Learning is a leading provider of digital curriculum and online courses to increase educational opportunities and achievement to students in grades K-12. Teachers and students access all course materials online.

School districts need greater visibility into the rate in which students are progressing through their courses, so school staff can better support students to complete courses at the required rate to keep them on track for graduation.
This can be accomplished by allowing school administrators to view a data dashboard and pull an on-demand report and see progress for a specified date range, relative to overall progress.

Within a specified date range, school administrators want to know if the student made more or less progress than in the period prior to the first date in the range.
School administrators also want to know if students are ahead or behind where they should be after the second date in the range.

Industry/Entity Type

Digital

```html
<!DOCTYPE html>
<html lang="en">
<head>
<meta charset="utf-8">
<title>Brightpath Learning Data Dashboard</title>
<link rel="stylesheet" href="https://fonts.googleapis.com/css2?family=Lato:wght@400;700&display=swap">
<style>
:root{
  --navy:#2b2556;
  --side:#333333;
  --side-line:#454545;
  --page:#f1f1f1;
  --white:#ffffff;
  --text:#222222;
  --line:#d6d6d6;
  --red:#d12030;
  --green:#2a991f;
  --download:#1f7a3a;
  --field-x:#d9d9d9;
}
*{box-sizing:border-box;margin:0;padding:0}
html,body{width:1200px;height:414px;overflow:hidden}
body{font-family:"Lato",sans-serif;color:var(--text);background:var(--page);position:relative}
.topbar{position:absolute;left:0;top:0;width:1200px;height:60px;background:var(--white)}
.brand{position:absolute;left:24px;top:21px;display:flex;align-items:center;gap:6px;color:var(--navy);font-weight:700;font-size:13px}
.brand-mark{width:14px;height:14px;background:var(--navy)}
.user{position:absolute;left:940px;top:18px;display:flex;align-items:center;gap:8px}
.avatar{width:24px;height:24px;border-radius:50%;background:#3a3a3a;display:flex;align-items:center;justify-content:center}
.user-text{font-size:10px;line-height:12px;color:#333}
.user-text strong{display:block;color:var(--navy);font-weight:700}
.download-btn{position:absolute;left:1068px;top:20px;width:106px;height:24px;border:1px solid #bbb;background:var(--white);color:var(--download);font-size:10px;display:flex;align-items:center;justify-content:center;gap:5px;white-space:nowrap}
.sidebar{position:absolute;left:0;top:60px;width:132px;height:354px;background:var(--side)}
.nav{list-style:none;padding-top:3px}
.nav li{height:33.3px;border-bottom:1px solid var(--side-line);display:flex;align-items:center;padding-left:20px;gap:8px;color:var(--white);font-size:9px;font-weight:700}
.nav svg{width:9px;height:9px;fill:var(--white)}
.copyright{position:absolute;left:20px;top:310px;color:var(--white);font-size:8px;line-height:13px}
.filter{position:absolute;top:71px}
.filter-label{font-size:8.4px;color:#333;height:13px;display:flex;align-items:center;gap:8px}
.radio{display:inline-flex;align-items:center;gap:3px}
.radio i{width:8px;height:8px;border:1px solid #aaa;border-radius:50%;background:var(--white);display:inline-block;position:relative}
.radio i.on::after{content:"";position:absolute;left:2px;top:2px;width:2px;height:2px;border-radius:50%;background:#333}
.field{display:flex;height:25px}
.select{width:200px;background:var(--white);border:1px solid #ddd;font-size:10px;color:#444;display:flex;align-items:center;justify-content:space-between;padding:0 8px}
.clear{width:30px;background:var(--field-x);display:flex;align-items:center;justify-content:center;font-size:11px;font-weight:700;color:var(--navy)}
.report{position:absolute;left:148px;top:118px;width:1026px;border-collapse:collapse;table-layout:fixed;background:var(--white);font-size:9px}
.report th{background:var(--navy);color:var(--white);font-weight:400;text-align:left;padding:0 8px;border:1px solid #56507a;font-size:10px;line-height:12px}
.report th.center{text-align:center;padding:0 3px}
.report th.sub{font-size:7.4px;text-align:center;padding:0;height:13px}
.report th.group{text-align:center;height:16px}
.report th.small{font-size:8.6px;text-align:center;padding:0 2px;height:19px}
.report td{height:30.7px;padding:0 8px;border:1px solid var(--line);line-height:10px}
.report td.red,.report td.green,.report td.rate{color:var(--white);text-align:center}
.report td.rate{color:var(--text)}
.red{background:var(--red)}
.green{background:var(--green)}
.report td.icon{text-align:center}
.report td.icon svg{width:18px;height:14px;fill:#444;vertical-align:middle}
</style>
</head>
<body>
<header class="topbar">
  <div class="brand"><span class="brand-mark"></span>Brightpath Learning</div>
  <div class="user">
    <div class="avatar"><svg width="12" height="12" viewBox="0 0 12 12"><circle cx="6" cy="4" r="2.4" fill="#fff"/><path d="M1.8 11c0-2.6 1.9-4 4.2-4s4.2 1.4 4.2 4z" fill="#fff"/></svg></div>
    <div class="user-text">Welcome User<strong>Dana Price</strong></div>
  </div>
  <div class="download-btn"><svg width="9" height="10" viewBox="0 0 9 10"><path d="M4.5 0v6M2 4l2.5 2.5L7 4" fill="none" stroke="#1f7a3a"/><path d="M0.5 8.5h8" stroke="#1f7a3a"/></svg>Spreadsheet Download</div>
</header>

<aside class="sidebar">
  <ul class="nav">
    <li><svg viewBox="0 0 10 10"><circle cx="4" cy="4" r="3" fill="none" stroke="#fff" stroke-width="1.6"/><path d="M6 6l3 3" stroke="#fff" stroke-width="1.8"/></svg>Search</li>
    <li><svg viewBox="0 0 10 10"><path d="M1 0h5l3 3v7H1z"/></svg>Course</li>
    <li><svg viewBox="0 0 10 10"><circle cx="3" cy="3" r="2"/><circle cx="7" cy="3" r="2"/><path d="M0 9c0-3 6-3 6 0zM4 9c0-3 6-3 6 0z"/></svg>Teacher</li>
    <li><svg viewBox="0 0 10 10"><rect x="1" y="1" width="8" height="9" fill="none" stroke="#fff"/><rect x="3" y="4" width="4" height="1"/></svg>Event</li>
    <li><svg viewBox="0 0 10 10"><path d="M2 0l2 2-1 2c1 1 2 2 3 3l2-1 2 2-2 2C4 9 1 6 0 2z"/></svg>Contact</li>
    <li><svg viewBox="0 0 10 10"><rect x="1" y="0" width="8" height="10"/></svg>School</li>
    <li><svg viewBox="0 0 10 10"><circle cx="5" cy="5" r="3.2" fill="none" stroke="#fff" stroke-width="2" stroke-dasharray="1.6 1"/><circle cx="5" cy="5" r="1.2"/></svg>Admin Setting</li>
  </ul>
  <p class="copyright">© 2018. Company Name.<br>All Right reserved</p>
</aside>

<div class="filter" style="left:148px">
  <div class="filter-label">School:</div>
  <div class="field"><div class="select">Choose a School <span>⇕</span></div><div class="clear">x</div></div>
</div>
<div class="filter" style="left:388px">
  <div class="filter-label"><span class="radio"><i class="on"></i>Observer</span><span class="radio"><i></i>Teacher</span></div>
  <div class="field"><div class="select">Choose a Observer <span>⇕</span></div><div class="clear">x</div></div>
</div>
<div class="filter" style="left:627px">
  <div class="filter-label">Filter Date 1</div>
  <div class="field"><div class="select">2/27/18 <span>⇕</span></div><div class="clear">x</div></div>
</div>
<div class="filter" style="left:867px">
  <div class="filter-label">Filter Date 2</div>
  <div class="field"><div class="select">3/6/18 <span>⇕</span></div><div class="clear">x</div></div>
</div>

<table class="report">
  <colgroup>
    <col style="width:84px"><col style="width:75px"><col style="width:58px"><col style="width:78px"><col style="width:50px"><col style="width:49px"><col style="width:62px"><col style="width:55px"><col style="width:50px"><col style="width:43px"><col style="width:50px"><col style="width:41px"><col style="width:70px"><col style="width:62px"><col style="width:74px"><col style="width:65px"><col style="width:60px">
  </colgroup>
  <thead>
    <tr>
      <th rowspan="3">Student Name</th><th rowspan="3">Observer</th><th rowspan="3">School</th><th rowspan="3">Course Title</th><th rowspan="3">Current Grade</th><th rowspan="3">Raw Score</th><th rowspan="3">Course Start Date</th><th rowspan="3">Course End Date</th>
      <th colspan="4" class="group">Percent &nbsp;&nbsp;&nbsp;&nbsp; Complete</th>
      <th rowspan="3" class="center">2/27-3/6 Progress Actual/ Goal</th><th rowspan="3" class="center">Status as of March 6</th><th rowspan="3" class="center">Completion Rate / day for the range</th><th rowspan="3" class="center">Completion Rate Change</th><th rowspan="3">Last<br>Login</th>
    </tr>
    <tr><th colspan="2" class="sub">Start – 2/27/18</th><th colspan="2" class="sub">End – 3/6/18</th></tr>
    <tr><th class="small">Actual %</th><th class="small">Goal %</th><th class="small">Actual %</th><th class="small">Goal %</th></tr>
  </thead>
  <tbody>
    <tr><td>Anthony Hale</td><td>Sam Ortiz</td><td>Ridgeview</td><td>Algebra 1A</td><td>67.3 %</td><td>67.3 %</td><td>2/20/18</td><td>2/20/18</td><td>0%</td><td>10%</td><td>0%</td><td>10%</td><td class="red">5/10</td><td class="red">5/10</td><td class="rate">.2%</td><td class="icon"><svg viewBox="0 0 18 14"><path d="M9 0l7 7h-4v7H6V7H2z"/></svg></td><td>3/6/18</td></tr>
    <tr><td>Jose Medina</td><td>Sam Ortiz</td><td>Ridgeview</td><td>Biology A</td><td>74.2%</td><td>74.2%</td><td>2/20/18</td><td>2/20/18</td><td>5%</td><td>10%</td><td>5%</td><td>10%</td><td class="green">10/10</td><td class="red">10/10</td><td class="rate">2.28%</td><td class="icon"><svg viewBox="0 0 18 14"><path d="M9 0l7 7h-4v7H6V7H2z"/></svg></td><td>3/6/18</td></tr>
    <tr><td>Maria Chen</td><td>Jema Castillo</td><td>Lakeside</td><td>US History A</td><td>82.3%</td><td>82.3%</td><td>2/20/18</td><td>2/20/18</td><td>15%</td><td>10%</td><td>15%</td><td>10%</td><td class="red">5/10</td><td class="green">5/10</td><td class="rate">7.14%</td><td class="icon"><svg viewBox="0 0 18 14"><path d="M9 14l7-7h-4V0H6v7H2z"/></svg></td><td>3/6/18</td></tr>
    <tr><td>Marcus Bell</td><td>Jema Castillo</td><td>Lakeside</td><td>Biology A</td><td>91.0%</td><td>91.0%</td><td>2/20/18</td><td>2/20/18</td><td>9%</td><td>10%</td><td>9%</td><td>10%</td><td class="red">5/10</td><td class="red">5/10</td><td class="rate">5%</td><td class="icon"><svg viewBox="0 0 18 14"><path d="M9 14l7-7h-4V0H6v7H2z"/></svg></td><td>3/6/18</td></tr>
    <tr><td>Juan Morales</td><td>Meg Dawson</td><td>Fairmont</td><td>Language Arts 10 A</td><td>94.5%</td><td>94.5%</td><td>2/20/18</td><td>2/20/18</td><td>11%</td><td>10%</td><td>11%</td><td>10%</td><td class="green">17/10</td><td class="green">17/10</td><td class="rate">2.8%</td><td class="icon"><svg viewBox="0 0 18 14"><path d="M9 0l7 7h-4v7H6V7H2z"/></svg></td><td>3/6/18</td></tr>
    <tr><td>Juan Morales</td><td>Meg Dawson</td><td>Fairmont</td><td>Language Arts 10 B</td><td>80%</td><td>80%</td><td>2/20/18</td><td>2/20/18</td><td>5%</td><td>10%</td><td>5%</td><td>10%</td><td class="red">5/10</td><td class="red">5/10</td><td class="rate">3%</td><td class="icon"><svg viewBox="0 0 26 14" style="width:24px"><path d="M0 7l7-7v4h12V0l7 7-7 7v-4H7v4z"/></svg></td><td>3/6/18</td></tr>
    <tr><td>Juan Morales</td><td>Meg Dawson</td><td>Fairmont</td><td>US History 1A</td><td>75%</td><td>75%</td><td>2/20/18</td><td>2/20/18</td><td>10%</td><td>10%</td><td>10%</td><td>10%</td><td class="green">10/10</td><td class="green">10/10</td><td class="rate">2%</td><td class="icon"><svg viewBox="0 0 26 14" style="width:24px"><path d="M0 7l7-7v4h12V0l7 7-7 7v-4H7v4z"/></svg></td><td>3/6/18</td></tr>
  </tbody>
</table>
</body>
</html>
```